Maplecrest Apartments Downtown Northport

We are looking to redesign our entry way sign at Maplecrest Apartments, a low density residential apartment building, located in Downtown Northport, Alabama, U.S. Downtown Northport is a bustling boutique business district with a small town feel comprised of shops, restaurants, and a renowned arts community known for Varrow Arts Center and Festival which is one of the nation's top outdoor arts festivals. Maplecrest Apartments and its sign is the first thing you seen when you enter Downtown Northport. We are looking to redesign our sign, entry way and landscaping to compliment the building and character of the historic downtown.

Target Market(s)

Our apartment building is comprised of 20 apartments units with tenants who are primarily part of the local workforce, young professionals, or students at the Halverton College or other nearby institutions.

Requirements
Must have
• The name of the apartment building - Maplecrest
Phone number on the sign 205-555-0148

```html
<!DOCTYPE html>
<html lang="en">
<head>
<meta charset="UTF-8">
<title>Maplecrest Apartments – Entry Sign</title>
<link rel="stylesheet" href="https://fonts.googleapis.com/css2?family=Playfair+Display:wght@700;800&display=swap">
<style>
  :root {
    --backdrop-light: #d6d6d6;
    --backdrop-dark: #a9a9a9;
    --board: #f1f1f0;
    --board-shade: #e2e2e1;
    --plank-seam: #c9c9c8;
    --wood-face: #b98a5e;
    --wood-edge-1: #7a4f3a;
    --wood-edge-2: #5e3a2c;
    --drop-shadow: rgba(0, 0, 0, 0.28);
  }
  html, body {
    margin: 0;
    padding: 0;
    width: 998px;
    height: 1200px;
    overflow: hidden;
  }
  body {
    background: radial-gradient(ellipse at 50% 35%, var(--backdrop-light) 0%, var(--backdrop-dark) 100%);
    position: relative;
    font-family: "Playfair Display", Georgia, serif;
  }
  .entry-sign {
    position: absolute;
    left: 75px;
    top: 440px;
    width: 848px;
    height: 340px;
    background: linear-gradient(180deg, var(--board) 0%, var(--board-shade) 100%);
    box-shadow: 14px 18px 26px var(--drop-shadow);
    overflow: hidden;
  }
  .plank-seams {
    position: absolute;
    inset: 0;
    width: 100%;
    height: 100%;
  }
  .sign-name {
    position: absolute;
    left: 0;
    right: 0;
    top: 58px;
    margin: 0;
    text-align: center;
    font-size: 124px;
    font-weight: 800;
    line-height: 1;
    letter-spacing: 1px;
    color: var(--wood-face);
    text-shadow:
      1px 1px 0 var(--wood-edge-1),
      2px 2px 0 var(--wood-edge-1),
      3px 3px 0 var(--wood-edge-2),
      4px 4px 0 var(--wood-edge-2),
      8px 12px 12px var(--drop-shadow);
  }
  .sign-phone {
    position: absolute;
    left: 0;
    right: 0;
    top: 232px;
    display: flex;
    justify-content: center;
    align-items: center;
    gap: 10px;
    font-size: 52px;
    font-weight: 700;
    line-height: 1;
    color: var(--wood-face);
    text-shadow:
      1px 1px 0 var(--wood-edge-1),
      2px 2px 0 var(--wood-edge-2),
      3px 3px 0 var(--wood-edge-2),
      6px 9px 9px var(--drop-shadow);
  }
  .phone-number {
    display: inline-block;
    transform: scaleX(0.82);
  }
  .phone-icon {
    width: 40px;
    height: 40px;
    filter: drop-shadow(2px 2px 0 var(--wood-edge-2)) drop-shadow(5px 7px 6px var(--drop-shadow));
  }
</style>
</head>
<body>
  <section class="entry-sign" aria-label="Maplecrest entry sign">
    <svg class="plank-seams" viewBox="0 0 848 340" preserveAspectRatio="none" aria-hidden="true">
      <g stroke="var(--plank-seam)" stroke-width="1.5">
        <line x1="90" y1="0" x2="90" y2="340"/>
        <line x1="188" y1="0" x2="188" y2="340"/>
        <line x1="281" y1="0" x2="281" y2="340"/>
        <line x1="380" y1="0" x2="380" y2="340"/>
        <line x1="475" y1="0" x2="475" y2="340"/>
        <line x1="572" y1="0" x2="572" y2="340"/>
        <line x1="668" y1="0" x2="668" y2="340"/>
        <line x1="766" y1="0" x2="766" y2="340"/>
      </g>
    </svg>
    <h1 class="sign-name">Maplecrest</h1>
    <div class="sign-phone">
      <svg class="phone-icon" viewBox="0 0 24 24" aria-hidden="true">
        <path fill="var(--wood-face)" d="M6.6 10.8c1.4 2.8 3.8 5.1 6.6 6.6l2.2-2.2c.3-.3.7-.4 1-.2 1.1.4 2.3.6 3.6.6.6 0 1 .4 1 1V20c0 .6-.4 1-1 1C10.6 21 3 13.4 3 4c0-.6.4-1 1-1h3.5c.6 0 1 .4 1 1 0 1.3.2 2.5.6 3.6.1.3 0 .7-.2 1L6.6 10.8z"/>
      </svg>
      <span class="phone-number">205-555-0148</span>
    </div>
  </section>
</body>
</html>
```